Home page web design for a lawn specialist business

-The design must be based around the attached HPID (home page information design) called Turf Tidings HPID. I've attached Word and PDF versions - these are the same. The table boxes are just for approximate placement of information and you can use boxes and bold shapes for this design.

All fonts used in the HPID are only examples - you can use any Google font you wish.

- Text that is in orange is for your information only. Text to go on the design is black. Some instructions are in the HPID. Please be creative!

-The design needs to be modern and exciting - colours are to be the green of the logo, and white ...and then choose dark green, or dark grey or black.

Logo - attached (it's not great quality but don't worry, we'll replace it later)

- I've provided the images for the galleries - they are labelled and will match the name in the HPID. Please use the supplied images!

- Examples of some websites that have great design... don't copy them please but they are similar in look to what we are after....
www.qmbbuildworks.co.nz
http://www.rim-safeguard.co.nz/
http://www.lumenhomes.wb.gs/

Important: Width of content will be 1280 pixels when implemented as a web page but the winning design will need to supplied be on a 2000 pixel wide background so nav bars and background can extend outside the 1280 width.
Header height (without nav bar) 150-160 pixels.

We don't comment on individual designs but will choose a winning design promptly.

Industry/Entity Type

Business

Number of Pages Required

1 page

Font styles to use
Sans Serif

Requirements
Must have
• clean, modern, well-spaced design

```html
<!DOCTYPE html>
<html lang="en">
<head>
<meta charset="utf-8">
<title>Turf Tidings – Lawn specialists</title>
<link href="https://fonts.googleapis.com/css2?family=Open+Sans:wght@400;600;700&family=Arimo:wght@400;700&display=swap" rel="stylesheet">
<style>
:root{
  --green:#2e9b3a;
  --green-bright:#3aa844;
  --nav:#78a50a;
  --nav-active:#a8cf30;
  --dark:#1d1d1b;
  --cream:#f0efb8;
  --frame:#f3f0a8;
  --panel:#dcefea;
  --ink:#111;
  --white:#fff;
}
*{box-sizing:border-box;margin:0;padding:0}
html,body{width:1200px;height:1000px;overflow:hidden}
body{position:relative;font-family:Arimo,Arial,sans-serif;color:var(--ink);
  background:linear-gradient(100deg,#c8e07a 0%,#e4f0c8 18%,#eef4ec 40%,#eaf2f2 65%,#cfe9f1 85%,#bfe2ef 100%)}
.header{position:absolute;left:0;top:0;width:1200px;height:96px;background:var(--white)}
.brand{position:absolute;left:217px;top:18px;display:flex;align-items:center;gap:12px}
.brand-mark{width:58px;height:58px;background:var(--green-bright)}
.brand-name{font-family:'Open Sans',sans-serif;font-weight:700;font-size:30px;color:var(--green)}
.tagline{position:absolute;right:217px;top:2px;text-align:right;font-family:'Open Sans',sans-serif;color:var(--green);line-height:1}
.tagline .title{font-size:28px;font-weight:600}
.tagline .title b{font-weight:700;color:#1e7a2a}
.tagline .sub{font-size:15px;font-weight:600;color:#1e7a2a;margin-top:4px}
.tagline .region{font-size:18px;margin-top:2px;color:#1e7a2a}
.tagline .phone{font-size:26px;font-weight:600;margin-top:2px;color:var(--green-bright)}
.nav{position:absolute;left:0;top:96px;width:1200px;height:51px;background:var(--nav)}
.nav ul{list-style:none;display:flex;position:absolute;left:217px;top:0;height:51px}
.nav li{font-family:'Open Sans',sans-serif;font-weight:600;font-size:13px;color:#111;padding:0 11px;line-height:51px}
.nav li.active{background:var(--nav-active)}
.hero{position:absolute;left:0;top:147px;width:1200px;height:303px;
  background:radial-gradient(circle at 50% 120%,#6c6c66 0%,#3d3d39 40%,#1e1e1c 80%)}
.hero-frame{position:absolute;left:240px;top:169px;width:718px;height:259px;border:3px solid var(--frame)}
.label{position:absolute;font-weight:700;font-size:18px;color:#000}
.intro{position:absolute;left:218px;top:451px;width:765px;height:165px;background:var(--panel);border:2px solid var(--white);padding:8px 12px;text-align:center}
.intro h1{font-family:'Open Sans',sans-serif;font-size:18px;font-weight:700}
.intro h1 em{color:var(--green-bright)}
.intro .lead{font-family:'Open Sans',sans-serif;font-size:15px;margin-top:2px}
.intro p.body{text-align:justify;font-size:12px;line-height:14px;margin-top:14px}
.card{position:absolute;width:374px;background:rgba(226,238,225,.85);border:2px solid var(--white);padding:6px 13px}
.card h2{background:var(--cream);height:46px;line-height:46px;text-align:center;font-size:17px;font-weight:700}
.card .photo{height:122px;border:3px solid var(--frame);margin-top:2px}
.card p{font-size:9.5px;font-weight:700;line-height:11.5px;margin-top:8px;text-align:justify}
.btn{display:block;width:fit-content;margin:4px auto 0;background:#000;color:#fff;font-size:11px;font-weight:700;padding:2px 4px}
</style>
</head>
<body>
<header class="header">
  <div class="brand"><div class="brand-mark"></div><span class="brand-name">Turf Tidings</span></div>
  <div class="tagline">
    <div class="title">Lawn <b>specialists</b></div>
    <div class="sub">... from ground preparation to lawn aftercare</div>
    <div class="region">Servicing the Auckland region</div>
    <div class="phone">0800 21 43 65</div>
  </div>
</header>
<nav class="nav"><ul>
  <li class="active">Home</li><li>About us</li><li>Services</li><li>Lawn care</li><li>Seasonal care</li><li>Hydroseeding</li><li>FAQs</li><li>Before &amp; After Gallery</li><li>Quote / Contact</li>
</ul></nav>
<section class="hero">
  <div class="hero-frame" style="left:240px;top:22px">
    <svg width="712" height="253" viewBox="0 0 712 253">
      <defs>
        <linearGradient id="before" x1="0" y1="0" x2="0" y2="1"><stop offset="0" stop-color="#e6e2da"/><stop offset=".35" stop-color="#7a6658"/><stop offset="1" stop-color="#5a4638"/></linearGradient>
        <linearGradient id="after" x1="0" y1="0" x2="0" y2="1"><stop offset="0" stop-color="#ebe8e0"/><stop offset=".35" stop-color="#4fb33a"/><stop offset="1" stop-color="#2f9a2a"/></linearGradient>
      </defs>
      <polygon role="img" aria-label="Courtyard with bare soil before lawn" points="0,0 378,0 318,253 0,253" fill="url(#before)"/>
      <polygon points="378,0 388,0 328,253 318,253" fill="#2a2a26"/>
      <polygon role="img" aria-label="Same courtyard with fresh green lawn after" points="388,0 712,0 712,253 328,253" fill="url(#after)"/>
    </svg>
    <span class="label" style="left:184px;top:196px">BEFORE</span>
    <span class="label" style="left:562px;top:196px">AFTER</span>
  </div>
</section>
<section class="intro">
  <h1>You can always spot an <em>Turf Tidings</em> lawn</h1>
  <p class="lead">It’s the one that turns your neighbours green with envy.</p>
  <p class="body">If you want a lawn or playing field that looks good throughout the year, talk to us. Turf Tidings are New Zealand’s experts in high quality grass seeding and lawn maintenance, creating the lushest lawns you’ll ever see. With high-tech equipment, years of experience and expert aftercare, nobody knows grass like Turf Tidings</p>
  <p class="body">There are many factors that influence the quality of a lawn, including seasonality, growing conditions, shade, seed types, and time. A one-size-fits-all solution couldn’t possibly guarantee a great lawn, so we provide personalised advice, a full range of seeding techniques</p>
</section>
<article class="card" style="left:218px;top:630px;height:248px">
  <h2>Grass seeding services</h2>
  <div class="photo" role="img" aria-label="Freshly hydroseeded garden lawn" style="background:linear-gradient(180deg,#6a7a5a 0%,#5c7a55 40%,#2f8a86 60%,#2a7a78 100%)"></div>
  <p>With a wide range of grass seed applications to choose from, including hydro-seeding and instant lawn, there is an option to suit your property and your requirements.</p>
  <span class="btn">MORE ABOUT GRASS SEEDING</span>
</article>
<article class="card" style="left:608px;top:630px;height:248px">
  <h2>Lawn care maintenance</h2>
  <div class="photo" role="img" aria-label="Sprinkler watering green grass" style="background:linear-gradient(180deg,#9fd08a 0%,#5fae3a 50%,#2f8a22 100%)"></div>
  <p>As well as lawn care services, the team at Turf Tidings provides helpful information for regular upkeep of your residential or commercial lawn.</p>
  <span class="btn">MORE ABOUT ONGOING LAWN CARE</span>
</article>
<article class="card" style="left:218px;top:892px;height:140px">
  <h2>FAQs about grass seeding and lawn care</h2>
  <div class="photo" role="img" aria-label="Backyard lawn with tree and fence" style="background:linear-gradient(180deg,#e6e0d2 0%,#b8b4a0 50%,#5aa640 100%)"></div>
</article>
<article class="card" style="left:608px;top:892px;height:140px">
  <h2>Before and after lawn photos</h2>
  <div class="photo" role="img" aria-label="Front yard of a house before lawn work" style="background:linear-gradient(180deg,#d8dce0 0%,#9a9a94 50%,#6e8a60 100%)"></div>
</article>
</body>
</html>
```